one side yoga classes, other side rental log cabin

I need a flyer to advertise yoga classes on a lake , and to describe the various styles of classes, and who they can benefit, Days Times .prices
Linked to it is a rental log cabin that can be rented privetly to families or Groups (8 max) www.fernvalestays.com This also is rented to yoga teacher that would like to Hire Cabin and the Studio www.velinoshaven.co.uk or
for Holistic weekends.

Teacher

```html
<!DOCTYPE html>
<html lang="en">
<head>
<meta charset="utf-8">
<title>Velinos Haven – Yoga Classes Flyer</title>
<link href="https://fonts.googleapis.com/css2?family=Questrial&family=Nunito+Sans:ital,wght@0,700;1,600&display=swap" rel="stylesheet">
<style>
  :root {
    --navy: #1c1c4f;
    --lavender: #d9d6ec;
    --lavender-deep: #b9b3da;
    --body-grey: #4a4a55;
    --white: #ffffff;
    --page-bg: #ffffff;
  }
  * { margin: 0; padding: 0; box-sizing: border-box; }
  html, body { width: 1200px; height: 1000px; overflow: hidden; background: var(--page-bg); }
  body { position: relative; font-family: "Questrial", sans-serif; }

  .flyer {
    position: absolute; top: 110px; width: 535px; height: 755px;
    overflow: hidden; box-shadow: 3px 4px 6px rgba(0,0,0,0.45);
    background: var(--white);
  }
  .flyer--classes { left: 55px; }
  .flyer--retreat { left: 620px; }

  .photo { position: absolute; }
  .flyer--classes .photo--studio {
    inset: 0;
    background: linear-gradient(180deg, #a9c4de 0%, #7e93a6 30%, #6b5646 55%, #8a5f3b 75%, #b98552 100%);
  }
  .flyer--retreat .photo--lake {
    left: 0; top: 0; width: 100%; height: 345px;
    background: linear-gradient(180deg, #b8d3ec 0%, #dfe9f2 30%, #6f8f4e 45%, #54703e 58%, #6f8fa8 70%, #4f6f8c 100%);
  }

  .title {
    position: absolute; left: 0; width: 100%; top: 40px; text-align: center;
    font-family: "Questrial", sans-serif; font-size: 44px; letter-spacing: 5px;
    color: var(--navy); font-weight: 400;
  }
  .flyer--classes .title { text-shadow: 0 0 6px #fff, 0 0 3px #fff; }

  .schedule {
    position: absolute; left: 25px; top: 106px; width: 490px;
    font-family: "Nunito Sans", sans-serif; font-weight: 700; font-size: 14.5px;
    line-height: 19px; color: var(--white);
    text-shadow: 1px 1px 2px rgba(0,0,0,0.75);
  }
  .schedule p { margin-bottom: 19px; }
  .schedule .note { font-style: italic; font-weight: 600; }

  .footer {
    position: absolute; left: 0; bottom: 0; width: 100%; height: 75px;
    background: var(--lavender);
    border-top: 4px solid var(--lavender-deep);
  }
  .footer__text {
    position: absolute; left: 30px; top: 18px; width: 230px; text-align: center;
    font-family: "Questrial", sans-serif; font-size: 10px; line-height: 14px; color: var(--navy);
  }

  .medallion {
    position: absolute; width: 190px; height: 190px; border-radius: 50%;
    border: 3px solid var(--lavender); overflow: hidden;
  }
  .flyer--classes .medallion { left: 350px; top: 600px;
    background: linear-gradient(180deg, #c4d3e2 0%, #b0593a 35%, #3b3330 60%, #b9a48a 100%); }
  .flyer--retreat .medallion { left: 345px; top: 578px;
    background: linear-gradient(180deg, #d9e4ee 0%, #3d4a4d 35%, #6d5a44 60%, #c9bca3 100%); }
  .medallion__caption {
    position: absolute; left: 0; top: 50px; width: 100%; text-align: center;
    font-family: "Questrial", sans-serif; font-size: 14px; line-height: 19px; color: var(--white);
    text-shadow: 1px 1px 2px rgba(0,0,0,0.8);
  }
  .medallion__caption .site { font-size: 12.5px; display: block; margin-top: 3px; }

  .themes {
    position: absolute; left: 0; top: 285px; width: 100%;
    display: flex; justify-content: space-around; padding: 0 28px;
    font-family: "Questrial", sans-serif; font-size: 25px; color: var(--white);
    text-shadow: 1px 1px 2px rgba(0,0,0,0.4);
  }
  .band--navy { position: absolute; left: 0; top: 345px; width: 100%; height: 30px; background: var(--navy); }
  .band--lavender { position: absolute; left: 0; top: 375px; width: 100%; height: 38px; background: var(--lavender); border-bottom: 3px solid var(--lavender-deep); }

  .intro {
    position: absolute; left: 27px; top: 428px; width: 450px;
    font-family: "Questrial", sans-serif; font-size: 14.5px; line-height: 21px; color: var(--body-grey);
  }
  .intro p { margin-bottom: 21px; }
  .intro .contact { font-size: 19.5px; color: var(--navy); margin-top: -18px; }
</style>
</head>
<body>

<section class="flyer flyer--classes">
  <div class="photo photo--studio" role="img" aria-label="Photo of a woman in a yoga pose on a mat in a wooden studio overlooking a lake"></div>
  <h1 class="title">YOGA CLASSES</h1>
  <div class="schedule">
    <p>Class schedule</p>
    <p>Tuesday - 8 am to 9.00 am Gentle Yoga for all - £7<br>(Velinos Studio)</p>
    <p>Tuesday - 10 am to 11.15am Dru Yoga - £7 (Velinos studio)</p>
    <p>Tuesday - 7.00pm to 8.15pm Hatha/Dru - £9<br>(Brambleham memorial Hall, Brambleham . Norfolk).<br>(Please note:- this class does not run on the first Tuesday of each month).</p>
    <p>Friday - 10am to 11.15 am Hatha Yoga - £7 (Velinos studio)</p>
    <p>Last Sunday of the month 8.30am to 10.00 Power Yoga &nbsp;- £10<br>(Velinos Studio)</p>
    <p class="note">A proportion of every class payment is put towards our supported charities</p>
    <p>For our events and retreats schedule please log into our web site<br>www.velinoshaven.co.uk</p>
    <p>The retreat can be hired by other teachers<br>and groups, so please call Marla on<br>07700 900412 for details.</p>
  </div>
  <footer class="footer">
    <div class="footer__text">Velinos Haven, 7 Alder Lakes, Alderby PE99 4ZZ<br>Tel: &nbsp;01632 960518<br>www.velinoshaven.co.uk</div>
  </footer>
  <div class="medallion" role="img" aria-label="Round photo of the wooden rental cabin with a tiled roof">
    <p class="medallion__caption">For details of<br>our on site rental<br>cabin go to<span class="site">www.fernvalestays.com</span></p>
  </div>
</section>

<section class="flyer flyer--retreat">
  <div class="photo photo--lake" role="img" aria-label="Photo of the retreat's wooden lodges on the shore of a lake under a blue sky"></div>
  <h1 class="title">VELINOS HAVEN</h1>
  <div class="themes"><span>Yoga</span><span>Meditation</span><span>Relaxation</span></div>
  <div class="band--navy"></div>
  <div class="band--lavender"></div>
  <div class="intro">
    <p>Velinos Haven is located on the shores of Alder Lakes, near Marshford, Norfolk. &nbsp;The retreat enjoys the surroundings of some of the most spectacular views in the UK with a bird and wildfowl sanctuary on our doorstep - perfect to relax and unwind for a few days away.</p>
    <p>For more retreat details and the gallery visit<br>our website www.velinoshaven.co.uk</p>
    <p class="contact">Contact Marla on 07700 900412</p>
  </div>
  <footer class="footer">
    <div class="footer__text">Velinos Haven, 7 Alder Lakes, Alderby PE99 4ZZ<br>Tel: &nbsp;01632 960518<br>www.velinoshaven.co.uk</div>
  </footer>
  <div class="medallion" role="img" aria-label="Round photo of an open wooden gazebo with seating beside the lake"></div>
</section>

</body>
</html>
```